Car dent,ding,crease removal. This will be for the Automotive industry, bodywork repair.

I need a double sided business card designing.

Company name is Panel Mender and we remove small car park dents creases and dings.

The card should have sleek car design/outline on it.

The wording Paintless Dent Removal to be on the card.

The background colours used should include Royal blue, black, and a hint of red.

Need a sleek modern look, clean lines.

I really don't want designers going to my website and just copying the car design, I want something new!

Reason: I've put a guaranteed payment on the design now.

Industry/Entity Type

Automotive

Requirements
Must have
• Paintless Dent Removal
Panel Mender
Gareth Holloway
enquiries@panelmender.example.co.uk
07700954316
Covering, Chester, North Wales and the Wirral
Free quotes available
www.panelmender.example.co.uk

```html
<!DOCTYPE html>
<html lang="en">
<head>
<meta charset="utf-8">
<title>Panel Mender – Business Card</title>
<link rel="stylesheet" href="https://fonts.googleapis.com/css2?family=Roboto:wght@300;400;700;900&display=swap">
<style>
  :root {
    --royal: #27479c;
    --royal-deep: #1d3783;
    --red: #c0272d;
    --red-deep: #a51f25;
    --white: #ffffff;
    --ink: #1b2a55;
    --backdrop: #e9e9ec;
  }
  * { box-sizing: border-box; margin: 0; padding: 0; }
  html, body { width: 1200px; height: 900px; overflow: hidden; }
  body {
    background: var(--backdrop);
    font-family: "Roboto", Arial, sans-serif;
    display: flex;
    align-items: center;
    justify-content: center;
    gap: 40px;
  }
  .card {
    position: relative;
    width: 540px;
    height: 340px;
    border-radius: 24px;
    overflow: hidden;
  }
  /* Front */
  .card-front {
    background: linear-gradient(180deg, var(--royal) 0%, var(--royal-deep) 100%);
    color: var(--white);
    display: flex;
    flex-direction: column;
    align-items: center;
    justify-content: center;
  }
  .brand-name {
    font-weight: 900;
    font-size: 58px;
    letter-spacing: -1px;
    line-height: 1;
  }
  .brand-tagline {
    font-weight: 300;
    font-size: 27px;
    margin-top: 6px;
    margin-left: 40px;
  }
  .coverage {
    position: absolute;
    bottom: 74px;
    left: 0;
    right: 0;
    text-align: center;
    font-size: 14px;
    font-weight: 400;
    letter-spacing: 0.2px;
  }
  /* Back */
  .card-back { background: var(--royal); }
  .card-back .panels { position: absolute; inset: 0; }
  .back-brand {
    position: absolute;
    top: 78px;
    left: 22px;
    width: 200px;
    color: var(--royal);
    text-align: center;
  }
  .back-brand .brand-name { font-size: 33px; letter-spacing: -0.5px; }
  .back-brand .brand-tagline { font-size: 15px; margin: 3px 0 0 18px; font-weight: 400; }
  .free-quotes {
    position: absolute;
    left: 0;
    top: 218px;
    width: 225px;
    text-align: center;
    color: var(--white);
    font-weight: 900;
    font-size: 25px;
    line-height: 1.05;
    text-transform: uppercase;
  }
  .contact {
    position: absolute;
    right: 28px;
    top: 60px;
    text-align: right;
    color: var(--white);
  }
  .contact-name {
    font-weight: 700;
    font-size: 20px;
    text-transform: uppercase;
    margin-bottom: 16px;
  }
  .contact-line { font-size: 13.5px; font-weight: 400; margin-bottom: 10px; }
  .contact-web { font-size: 14px; font-weight: 700; margin-top: 16px; }
</style>
</head>
<body>
  <section class="card card-front">
    <div class="brand-name">Panel Mender</div>
    <div class="brand-tagline">Paintless Dent Removal</div>
    <p class="coverage">Covering, Chester, North Wales and the Wirral</p>
  </section>

  <section class="card card-back">
    <svg class="panels" width="540" height="340" viewBox="0 0 540 340" aria-hidden="true">
      <polygon points="0,0 215,0 232,195 0,195" fill="var(--white)"/>
      <polygon points="0,195 232,195 245,340 0,340" fill="var(--red)"/>
    </svg>
    <div class="back-brand">
      <div class="brand-name">Panel Mender</div>
      <div class="brand-tagline">Paintless Dent Removal</div>
    </div>
    <p class="free-quotes">Free Quotes<br>Available</p>
    <div class="contact">
      <p class="contact-name">Gareth Holloway</p>
      <p class="contact-line">07700954316</p>
      <p class="contact-line">enquiries@panelmender.example.co.uk</p>
      <p class="contact-web">www.panelmender.example.co.uk</p>
    </div>
  </section>
</body>
</html>
```